Gather: Flu Poster (1 page)

We are looking to create a 11 by 17 inch 1 page poster.
-- Please Include KR7’s logo
-- Use the colors and font and mimic the feel of from Bright Mornings, Steady Steps Toolkit - Memory Care Prevention Leaflets - Northern Council for Tribal Longevity (kronsevel.org)
--> https://kronsevel.org/toolkit-memory-care-prevention-leaflets/
Moto needs to be included and it is: Protect Your Community. Protect Your Elders. Stay Vaccinated.
Include funding statement at the bottom of document - small print:
This project is supported by the Bureau for Illness Tracking and Wellness Planning of the U.S. Office of Public Welfare and Family Support (OPW) as part of a financial assistance award totaling $20,007,444 with 100 percent funded by BIT/OPW. The contents are those of the author(s) and do not necessarily represent the official views of, nor an endorsement, by BIT/OPW, or the U.S. Government.

```html
<!DOCTYPE html>
<html lang="en">
<head>
<meta charset="utf-8">
<title>Gather – Fight the Flu Poster</title>
<link rel="stylesheet" href="https://fonts.googleapis.com/css2?family=Montserrat:wght@400;500;600;700;800;900&display=swap">
<style>
  :root {
    --paper: #f3e6d4;
    --paper-clear: rgba(243,230,212,0);
    --teal: #4aa3ad;
    --teal-dark: #1f6b70;
    --brown: #5a3110;
    --maroon: #9b3a40;
    --ink: #4a2f1f;
    --band: #c27c78;
    --white: #ffffff;
  }
  * { box-sizing: border-box; margin: 0; padding: 0; }
  html, body { width: 776px; height: 1200px; overflow: hidden; background: var(--paper); }
  body { font-family: "Montserrat", Arial, sans-serif; color: var(--ink); }

  .poster { position: relative; width: 776px; height: 1200px; background: var(--paper); overflow: hidden; }

  .campaign-title {
    position: absolute; left: 39px; top: 27px; width: 521px; height: 106px;
    border: 4px solid var(--white);
    display: flex; align-items: center; justify-content: center;
    font-weight: 800; font-size: 80px; letter-spacing: 9px; padding-left: 9px;
    color: var(--teal); line-height: 1;
  }

  .brand {
    position: absolute; left: 624px; top: 40px; width: 126px; height: 80px;
    display: flex; align-items: center; justify-content: center; gap: 8px;
    font-weight: 800; font-size: 50px; color: var(--teal); line-height: 1;
  }
  .brand-dot { width: 12px; height: 12px; border-radius: 50%; background: var(--teal); }

  .photo {
    position: absolute; left: 0; top: 250px; width: 776px; height: 415px; z-index: 1;
    background:
      linear-gradient(to bottom, var(--paper) 0%, var(--paper-clear) 12%, var(--paper-clear) 80%, var(--paper) 100%),
      linear-gradient(100deg, #b8552e 0%, #8a4a2e 22%, #e9dccb 40%, #2e3440 55%, #b5462f 68%, #6b3a8a 85%, #d9cbbb 100%);
  }

  .motto { position: absolute; left: 0; width: 776px; text-align: center; font-weight: 800; color: var(--brown); line-height: 1; z-index: 2; }
  .motto-community { top: 163px; font-size: 52px; letter-spacing: 1px; }
  .motto-elders { top: 211px; font-size: 60px; letter-spacing: 1px; }
  .motto-elders .accent { color: var(--maroon); }

  .stay-vaccinated {
    position: absolute; left: 0; top: 586px; width: 776px; text-align: center; z-index: 2;
    padding-left: 16px;
    font-weight: 800; font-size: 50px; color: var(--white); line-height: 1;
  }

  .info { position: absolute; left: 70px; width: 660px; z-index: 2; }
  .info h2 { font-weight: 700; font-size: 13.6px; color: var(--teal-dark); line-height: 1.25; }
  .info ul { list-style: none; margin-top: 13px; }
  .info li { font-size: 12.2px; line-height: 15.3px; font-weight: 500; color: var(--ink); padding-left: 9px; position: relative; }
  .info li::before {
    content: ""; position: absolute; left: 0; top: 5.5px; width: 4px; height: 4px;
    background: var(--teal); transform: rotate(45deg);
  }
  .info-risk { top: 668px; }
  .info-symptoms { top: 800px; }
  .info-symptoms ul { margin-top: 11px; }
  .info-prevent { top: 962px; }

  .call-to-action {
    position: absolute; left: 0; top: 1072px; width: 776px; text-align: center;
    font-weight: 800; font-size: 50px; letter-spacing: 1px; line-height: 1; color: var(--teal-dark);
  }
  .call-to-action .accent { color: var(--maroon); }

  .funding {
    position: absolute; left: 0; top: 1128px; width: 776px; height: 60px;
    background: var(--band); color: var(--white);
    display: flex; align-items: center; justify-content: center; text-align: center;
    padding: 0 56px; font-size: 11.2px; line-height: 12.6px; font-weight: 500;
  }
</style>
</head>
<body>
<main class="poster">
  <div class="campaign-title">GATHER</div>

  <div class="brand" aria-label="KR7">
    <span class="brand-name">KR7</span>
    <span class="brand-dot"></span>
  </div>

  <div class="photo" role="img" aria-label="Photograph of three generations of Native women and children wrapped in colorful woven blankets and wearing turquoise jewelry, smiling together outdoors"></div>

  <h1 class="motto motto-community">Protect Your Community</h1>
  <p class="motto motto-elders">Protect Your <span class="accent">Elders</span></p>

  <p class="stay-vaccinated">Stay Vaccinated.</p>

  <section class="info info-risk">
    <h2>American Indian and Alaska Native people face higher risks from the flu.</h2>
    <ul>
      <li>Anyone can catch the flu.</li>
      <li>Native elders are at a higher risk of death from the flu and pneumonia.</li>
      <li>The flu vaccine is safe.</li>
      <li>You can’t get the flu from the vaccine.</li>
      <li>Get vaccinated for the flu every year to protect yourself and your loved ones<br>from being exposed to the influenza virus.</li>
    </ul>
  </section>

  <section class="info info-symptoms">
    <h2>Signs &amp; Symptoms of the Flu (may take 1 to 4 days to appear after exposure to the virus, and symptoms may include)</h2>
    <ul>
      <li>Fever or feeling feverish/chills; though not everyone will have a fever</li>
      <li>Cough</li>
      <li>Muscle or body aches</li>
      <li>Fatigue (feeling very tired)</li>
      <li>Sore throat</li>
      <li>Headache</li>
      <li>Vomiting or diarrhea; mostly common in children</li>
    </ul>
  </section>

  <section class="info info-prevent">
    <h2>Help Prevent the Spead of the Flu</h2>
    <ul>
      <li>Get the flu vaccine every year.</li>
      <li>Cover your mouth when you cough or sneeze.</li>
      <li>Wash your hands.</li>
      <li>Stay home if you are sick.</li>
      <li>See the doctor for treatment that you are prescribed.</li>
    </ul>
  </section>

  <p class="call-to-action"><span class="accent">Fight</span> the Flu!</p>

  <footer class="funding">
    This project is supported by the Bureau for Illness Tracking and Wellness Planning of the U.S. Office of Public Welfare and Family Support (OPW) as part of a financial assistance award totaling $20,007,444 with 100 percent funded by BIT/OPW. The contents are those of the author(s) and do not necessarily represent the official views of, nor an endorsement, by BIT/OPW, or the U.S. Government.
  </footer>
</main>
</body>
</html>
```